Tech Company Letterhead/Business Cards/Envelopes

We would like a new stationary design for a technology company that develops full turnkey solutions for governments related to Data, Identity Tracking, Fingerprinting, Passport Control, and Border Protection Systems.

We would like the stationary designs to include:

Letter Head
Business Cards
Envelopes

Target Market(s)

Corporate

Industry/Entity Type

Business

Contact Information for Business Card

Details to be shared with the winner.

Font styles to use
Serif
Sans Serif

Colors
e4daeb
85abd2
3176b5
0355a3
0692cd

```html
<!DOCTYPE html>
<html lang="en">
<head>
<meta charset="utf-8">
<title>Vortel Business Card</title>
<link rel="stylesheet" href="https://fonts.googleapis.com/css2?family=Didact+Gothic&display=swap">
<style>
  :root {
    --page-bg: #e9e6e3;
    --card-bg: #1b1b1d;
    --brand-blue: #0692cd;
    --accent-blue: #3176b5;
    --text-grey: #8a8a8c;
    --name-grey: #6d6d70;
  }
  * { margin: 0; padding: 0; box-sizing: border-box; }
  html, body {
    width: 1200px;
    height: 716px;
    overflow: hidden;
    background: var(--page-bg);
    font-family: "Didact Gothic", sans-serif;
  }
  .canvas {
    position: relative;
    width: 1200px;
    height: 716px;
    display: flex;
    align-items: center;
    justify-content: center;
    gap: 48px;
  }
  .card {
    position: relative;
    width: 540px;
    height: 309px;
    background: var(--card-bg);
    border-radius: 4px;
    box-shadow: 0 10px 30px rgba(0, 0, 0, 0.25);
    overflow: hidden;
  }
  .card-front .wordmark {
    position: absolute;
    left: 0;
    right: 0;
    top: 50%;
    transform: translateY(-50%);
    text-align: center;
    font-size: 64px;
    letter-spacing: 10px;
    color: var(--name-grey);
  }
  .card-back .wordmark {
    position: absolute;
    right: 36px;
    top: 34px;
    font-size: 46px;
    letter-spacing: 7px;
    color: var(--brand-blue);
  }
  .identity {
    position: absolute;
    right: 36px;
    top: 104px;
    width: 230px;
    text-align: right;
  }
  .employee-name {
    font-size: 17px;
    letter-spacing: 1px;
    color: var(--brand-blue);
    text-align: left;
    padding-bottom: 6px;
    border-bottom: 2px solid var(--accent-blue);
  }
  .employee-title {
    margin-top: 4px;
    font-size: 16px;
    color: var(--text-grey);
  }
  .contact-list {
    position: absolute;
    right: 36px;
    top: 170px;
    list-style: none;
    text-align: right;
    font-size: 14px;
    line-height: 19px;
    color: var(--text-grey);
  }
  .contact-list li {
    display: flex;
    justify-content: flex-end;
    align-items: center;
    gap: 7px;
  }
  .contact-list .icon {
    width: 12px;
    height: 12px;
    fill: var(--brand-blue);
    stroke: var(--brand-blue);
  }
  .contact-list .address {
    display: block;
    margin-top: 6px;
    padding-right: 19px;
  }
</style>
</head>
<body>
<main class="canvas">
  <section class="card card-front">
    <div class="wordmark">VORTEL</div>
  </section>

  <section class="card card-back">
    <div class="wordmark">VORTEL</div>
    <div class="identity">
      <div class="employee-name">EMPLOYEE NAME</div>
      <div class="employee-title">Title</div>
    </div>
    <ul class="contact-list">
      <li>800.555.0142
        <svg class="icon" viewBox="0 0 12 12" aria-hidden="true"><path stroke="none" d="M2.5 1 L4.5 1 L5 3.5 L3.8 4.5 Q5 7 7.5 8.2 L8.5 7 L11 7.5 L11 9.5 Q11 11 9.5 11 Q1 10 1 2.5 Q1 1 2.5 1Z"/></svg>
      </li>
      <li>800.555.0199
        <svg class="icon" viewBox="0 0 12 12" aria-hidden="true"><rect stroke="none" x="3" y="1" width="6" height="3"/><rect stroke="none" x="1" y="4.5" width="10" height="4.5" rx="1"/><rect stroke="none" x="3" y="8" width="6" height="3"/></svg>
      </li>
      <li>hello@vortel-id.com
        <svg class="icon" viewBox="0 0 12 12" aria-hidden="true"><rect stroke="none" x="0.5" y="2.5" width="11" height="7"/><path fill="none" stroke="#1b1b1d" stroke-width="1" d="M0.8 2.8 L6 7 L11.2 2.8"/></svg>
      </li>
      <li>www.vortel-id.com
        <svg class="icon" viewBox="0 0 12 12" aria-hidden="true"><g fill="none" stroke-width="1"><circle cx="6" cy="6" r="5"/><ellipse cx="6" cy="6" rx="2.2" ry="5"/><path d="M1 6 H11 M2 3.5 H10 M2 8.5 H10"/></g></svg>
      </li>
      <li class="address">48 Harbor Row Suite 210,<br>Fairview USA 40215</li>
    </ul>
  </section>
</main>
</body>
</html>
```